Software Development Consulting Company Needs Business Card Design

We need a new business card design for our consultants at Verdant Systems (verdantsystems.example). We are a small firm that provides high-end software development and methodology consulting to medium to large enterprise IT organizations.

Our logo uses Futura for the font and we would like to stick with navy blue and canary yellow for the logo colors. Attached are normal and reversed versions of our logos in illustrator format.
Updates

Hi Everyone, Thank yo very much for your amazing design ideas. I have created a poll for this project and our employees will be voting on the design they wish to use. We will be making a decision this Wednesday (October 22nd). Thanks again, Marcus Hallward

Industry/Entity Type

Business

```html
<!DOCTYPE html>
<html lang="en">
<head>
<meta charset="utf-8">
<title>Verdant Systems – Business Card</title>
<link rel="stylesheet" href="https://fonts.googleapis.com/css2?family=Jost:wght@400;500&display=swap">
<style>
  :root {
    --page-bg: #d9d9d9;
    --card-white: #ffffff;
    --brand-navy: #1f3a68;
    --brand-navy-light: #4d6a99;
    --accent-grey: #d7d8dc;
    --accent-yellow: #f5df1b;
    --text-on-navy: #ffffff;
  }
  * { box-sizing: border-box; margin: 0; padding: 0; }
  html, body {
    width: 1200px;
    height: 675px;
    overflow: hidden;
    background: var(--page-bg);
    font-family: "Jost", "Futura", sans-serif;
  }
  .canvas {
    position: relative;
    width: 1200px;
    height: 675px;
  }
  .card {
    position: absolute;
    top: 195px;
    width: 500px;
    height: 286px;
    background: var(--card-white);
    overflow: hidden;
    box-shadow: 0 2px 6px rgba(0,0,0,0.12);
  }
  .card--front { left: 70px; }
  .card--back { left: 630px; }

  .card__shapes {
    position: absolute;
    inset: 0;
    width: 100%;
    height: 100%;
  }

  .contact {
    position: absolute;
    left: 26px;
    top: 24px;
    color: var(--text-on-navy);
  }
  .contact__name {
    font-size: 20px;
    font-weight: 500;
    line-height: 1.1;
  }
  .contact__title {
    font-size: 12px;
    font-weight: 400;
    margin-top: 2px;
  }
  .contact__list {
    list-style: none;
    margin-top: 18px;
    font-size: 11px;
    line-height: 1.55;
  }
  .contact__label {
    font-weight: 500;
    font-size: 13px;
  }
  .contact__address {
    display: flex;
    align-items: center;
    gap: 5px;
  }
  .contact__pin { width: 9px; height: 12px; fill: var(--text-on-navy); }

  .wordmark {
    position: absolute;
    display: flex;
    align-items: center;
    color: var(--brand-navy);
    font-weight: 500;
    text-transform: uppercase;
    white-space: nowrap;
  }
  .wordmark__dot {
    border-radius: 50%;
    background: var(--accent-yellow);
    flex: none;
  }
  .wordmark--small {
    left: 318px;
    top: 79px;
    font-size: 12px;
    letter-spacing: 1.5px;
    gap: 6px;
  }
  .wordmark--small .wordmark__dot { width: 7px; height: 7px; }
  .wordmark--large {
    left: 50%;
    top: 50%;
    transform: translate(-50%, -50%);
    font-size: 34px;
    letter-spacing: 5px;
    gap: 14px;
  }
  .wordmark--large .wordmark__dot { width: 14px; height: 14px; }
</style>
</head>
<body>
<main class="canvas">

  <section class="card card--front" aria-label="Business card front">
    <svg class="card__shapes" viewBox="0 0 500 286" preserveAspectRatio="none" aria-hidden="true">
      <rect class="band-navy" x="0" y="0" width="500" height="215" fill="var(--brand-navy)"/>
      <rect class="band-white" x="0" y="215" width="500" height="71" fill="var(--card-white)"/>
      <rect class="block-light" x="265" y="170" width="235" height="116" fill="var(--brand-navy-light)"/>
      <polygon class="logo-panel" points="312,48 500,48 500,128 300,128 300,60" fill="var(--card-white)"/>
      <polygon class="hex-accent" points="280,128 345,128 345,200 300,232 265,232 265,150" fill="var(--accent-grey)"/>
    </svg>

    <div class="contact">
      <h1 class="contact__name">Marcus Hallward</h1>
      <p class="contact__title">Principal Consultant</p>
      <ul class="contact__list">
        <li><span class="contact__label">M</span> : 555-210-7788</li>
        <li><span class="contact__label">T</span> : @mhallward</li>
        <li><span class="contact__label">E</span> : marcus.hallward@verdantsystems.example</li>
        <li><span class="contact__label">W</span> : www.verdantsystems.example</li>
        <li class="contact__address">
          <svg class="contact__pin" viewBox="0 0 12 16" aria-hidden="true"><path d="M6 0a6 6 0 0 0-6 6c0 4.5 6 10 6 10s6-5.5 6-10a6 6 0 0 0-6-6zm0 8.3A2.3 2.3 0 1 1 6 3.7a2.3 2.3 0 0 1 0 4.6z"/></svg>
          2400 Meadow Park Ln, Fairview, MO 63000
        </li>
      </ul>
    </div>

    <div class="wordmark wordmark--small">
      <span class="wordmark__dot"></span>
      <span class="wordmark__name">Verdant Systems</span>
    </div>
  </section>

  <section class="card card--back" aria-label="Business card back">
    <div class="wordmark wordmark--large">
      <span class="wordmark__dot"></span>
      <span class="wordmark__name">Verdant Systems</span>
    </div>
  </section>

</main>
</body>
</html>
```